CD Cover Artwork for Classical Music Cover

We are about to launch 13 CDs online for digital downloads and require artwork for the accompanying CD covers. As the covers will not be printed, we only require web-optimized artwork. We are fine with one standard template that can be adapted for all the covers. The only differentiating factors will be the colour of the covers and the title information. We need to create a more progressive, eye-catching design than the below examples which we have been promoting through our website until now. You have full liberties to come up with whatever design you think is more appropriate and to use whatever fonts and juxtaposition of content and images as you see fit.
ARTIST INFORMATION: Harold Venmark was an American composer who lived and worked his entire life in New York City. He was a 1930 Marlowe Conservatory graduate and studied composition with Milton Brasher, Lew Doddard, Pemberton Quillock and Walter Pennimore. In a 1947 competition, with Karl Estergaard as one of three jurors, Venmark’s "Harbor Prelude" won First Prize. He produced a large body of work comprising hundreds of compositions across diverse musical genres ... From 2001 to early 2008, Harold Venmark’s music came to life through a unique collaboration with many of the finest musicians in St. Petersburg, Russia. Nearly all of Venmark’s musical repertoire was transcribed from their original manuscripts to electronic form. And dozens of recording sessions produced 13 CDs, including all his chambers works, many piano concertos and symphonies, and works for horn, flute, strings and woodwinds. This “musical discovery” was the brainchild of his late son, Thomas Venmark.
ARTIST WEBSITE: www.haroldvenmark.com
FACEBOOK PAGE: https://www.facebook.com/pages/Harold-Venmark-A-Hidden-Chapter-of-Concert-Song/582910374615208
ATTACHMENTS:
- A few images of Harold Venmark (young and old)
- List of CD information along with a visual representation of the information that should be included
Target Market(s)
Classical music lovers the world over
Industry/Entity Type
Electronic
Look and feel

```html
<!DOCTYPE html>
<html lang="en">
<head>
<meta charset="utf-8">
<title>Harold Venmark – CD Cover Series</title>
<link rel="stylesheet" href="https://fonts.googleapis.com/css2?family=Anton&family=Arimo:wght@400&display=swap">
<style>
  :root {
    --page: #ffffff;
    --royal: #283593;
    --ink: #050505;
    --paper: #ffffff;
    --portrait-blue-a: #3a47a8;
    --portrait-blue-b: #dfe2f2;
    --portrait-black-a: #1a1a1a;
    --portrait-black-b: #e6e6e6;
    --shadow: rgba(0, 0, 0, 0.5);
  }
  * { margin: 0; padding: 0; box-sizing: border-box; }
  html, body { width: 1200px; height: 1000px; overflow: hidden; background: var(--page); }
  .canvas { position: relative; width: 1200px; height: 1000px; }

  .cover-slot { position: absolute; }
  .cover-slot--blue-large { left: 44px; top: 44px; }
  .cover-slot--black-large { left: 634px; top: 44px; }
  .cover-slot--blue-small { left: 177px; top: 657px; width: 265.5px; height: 265.5px; }
  .cover-slot--black-small { left: 767px; top: 657px; width: 265.5px; height: 265.5px; }
  .cover-slot--blue-small .cover,
  .cover-slot--black-small .cover { transform: scale(0.5); transform-origin: 0 0; }

  .cover {
    position: relative;
    width: 531px; height: 531px;
    background: var(--cover-colour);
    box-shadow: 9px 9px 7px var(--shadow);
    overflow: hidden;
    color: var(--paper);
  }
  .cover--blue { --cover-colour: var(--royal); --accent: var(--royal); --p-a: var(--portrait-blue-a); --p-b: var(--portrait-blue-b); }
  .cover--black { --cover-colour: var(--ink); --accent: var(--ink); --p-a: var(--portrait-black-a); --p-b: var(--portrait-black-b); }

  .composer {
    position: absolute; left: 25px; top: 16px;
    font-family: "Anton", "Impact", sans-serif;
    font-weight: 400;
    color: var(--paper);
  }
  .composer__name { font-size: 54px; line-height: 66px; letter-spacing: 0.5px; }
  .composer__dates { font-size: 34px; line-height: 44px; margin-top: 2px; }
  .tagline {
    position: absolute; left: 53px; top: 211px;
    font-family: "Anton", "Impact", sans-serif;
    font-size: 14px; letter-spacing: 0.1px;
  }

  .series-title {
    position: absolute; left: 53px; top: 465px;
    font-family: "Anton", "Impact", sans-serif;
    font-size: 17px; line-height: 23px;
  }

  .side-panel {
    position: absolute; left: 371px; top: 0;
    width: 160px; height: 531px;
    background: var(--paper);
    color: var(--accent);
  }
  .portrait {
    position: absolute; left: 0; top: 0; width: 160px; height: 199px;
    background: linear-gradient(160deg, var(--p-b) 0%, var(--p-a) 70%);
  }
  .publisher {
    position: absolute; left: 0; top: 212px; width: 160px;
    text-align: center;
    font-family: "Anton", "Impact", sans-serif;
    font-size: 16px; line-height: 22px; letter-spacing: 2.6px;
  }
  .publisher__first { letter-spacing: 7px; }
  .disc-number {
    position: absolute; left: 0; top: 452px; width: 160px;
    text-align: center;
    font-family: "Anton", "Impact", sans-serif;
    font-size: 42px; line-height: 60px;
  }

  .track-list, .performer-list {
    position: absolute;
    font-family: "Arimo", "Arial", sans-serif;
    font-size: 12px; line-height: 15px;
  }
  .track-list--works { left: 25px; top: 251px; }
  .track-list--details { left: 199px; top: 251px; }
  .performer-list { left: 14px; top: 296px; color: var(--ink); }
</style>
</head>
<body>
<main class="canvas">

  <!-- Chamber works, large -->
  <div class="cover-slot cover-slot--blue-large">
    <section class="cover cover--blue">
      <div class="composer">
        <div class="composer__name">Harold<br>Venmark</div>
        <div class="composer__dates">1905 - 1986</div>
      </div>
      <p class="tagline">“A Hidden Chapter of Concert Song”</p>
      <p class="series-title">Selected<br>Chamber Works (a)</p>
      <aside class="side-panel">
        <div class="portrait" role="img" aria-label="Stylised portrait of the composer Harold Venmark in a bow tie"></div>
        <p class="publisher"><span class="publisher__first">Lindmer</span><br>Publishing</p>
        <p class="disc-number">CD 01</p>
      </aside>
    </section>
  </div>

  <!-- Clarinet & oboe, large -->
  <div class="cover-slot cover-slot--black-large">
    <section class="cover cover--black">
      <div class="composer">
        <div class="composer__name">Harold<br>Venmark</div>
        <div class="composer__dates">1905 - 1986</div>
      </div>
      <p class="tagline">“A Hidden Chapter of Concert Song”</p>
      <p class="track-list track-list--works">Two Sonatas for Clarinet<br>and Piano<br>Three Movements foTwo<br>Sonatas for Clarinet and<br>Piano<br>Three Movements for Two<br>Oboes and Piano<br>Duets for Two Clarinets<br>Divertimento for Wind<br>Quartet<br>Sonata for Five Clarinets</p>
      <p class="track-list track-list--details">Clarinets: D. Orlenko, A.<br>Brantsev, A. Velikov, V.<br>Dremin, M. Shustin, A.<br>Kornilov, I. Tarel-<br>kin, A. Zhuravin<br>Oboes: A. Pellin, A. Rudakov<br>Piano: P. Mirovsky<br>Two Oboes and Piano<br>Duets for Two Clarinets<br>Divertimento for Wind<br>Quartet<br>Sonata for Five Clarinets</p>
      <p class="series-title">Works for<br>Clarinet &amp; Oboe</p>
      <aside class="side-panel">
        <div class="portrait" role="img" aria-label="Stylised portrait of the composer Harold Venmark in a bow tie"></div>
        <p class="publisher"><span class="publisher__first">Lindmer</span><br>Publishing</p>
        <p class="performer-list">Clarinets: D. Orlenko,<br>A. Brantsev, A. Velikov,<br>V. Dremin, M. Shustin,<br>A. Kornilov,<br>I. Tarelkin,<br>A. Zhuravin<br>Oboes:&nbsp; A. Pellin,<br>A. Rudakov<br>Piano: P. Mirovsky</p>
        <p class="disc-number">CD 07</p>
      </aside>
    </section>
  </div>

  <!-- Chamber works, thumbnail -->
  <div class="cover-slot cover-slot--blue-small">
    <section class="cover cover--blue">
      <div class="composer">
        <div class="composer__name">Harold<br>Venmark</div>
        <div class="composer__dates">1905 - 1986</div>
      </div>
      <p class="tagline">“A Hidden Chapter of Concert Song”</p>
      <p class="series-title">Selected<br>Chamber Works (a)</p>
      <aside class="side-panel">
        <div class="portrait" role="img" aria-label="Stylised portrait of the composer Harold Venmark in a bow tie"></div>
        <p class="publisher"><span class="publisher__first">Lindmer</span><br>Publishing</p>
        <p class="disc-number">CD 01</p>
      </aside>
    </section>
  </div>

  <!-- Clarinet & oboe, thumbnail -->
  <div class="cover-slot cover-slot--black-small">
    <section class="cover cover--black">
      <div class="composer">
        <div class="composer__name">Harold<br>Venmark</div>
        <div class="composer__dates">1905 - 1986</div>
      </div>
      <p class="tagline">“A Hidden Chapter of Concert Song”</p>
      <p class="track-list track-list--works">Two Sonatas for Clarinet<br>and Piano<br>Three Movements foTwo<br>Sonatas for Clarinet and<br>Piano<br>Three Movements for Two<br>Oboes and Piano<br>Duets for Two Clarinets<br>Divertimento for Wind<br>Quartet<br>Sonata for Five Clarinets</p>
      <p class="track-list track-list--details">Clarinets: D. Orlenko, A.<br>Brantsev, A. Velikov, V.<br>Dremin, M. Shustin, A.<br>Kornilov, I. Tarel-<br>kin, A. Zhuravin<br>Oboes: A. Pellin, A. Rudakov<br>Piano: P. Mirovsky<br>Two Oboes and Piano<br>Duets for Two Clarinets<br>Divertimento for Wind<br>Quartet<br>Sonata for Five Clarinets</p>
      <p class="series-title">Works for<br>Clarinet &amp; Oboe</p>
      <aside class="side-panel">
        <div class="portrait" role="img" aria-label="Stylised portrait of the composer Harold Venmark in a bow tie"></div>
        <p class="publisher"><span class="publisher__first">Lindmer</span><br>Publishing</p>
        <p class="performer-list">Clarinets: D. Orlenko,<br>A. Brantsev, A. Velikov,<br>V. Dremin, M. Shustin,<br>A. Kornilov,<br>I. Tarelkin,<br>A. Zhuravin<br>Oboes:&nbsp; A. Pellin,<br>A. Rudakov<br>Piano: P. Mirovsky</p>
        <p class="disc-number">CD 07</p>
      </aside>
    </section>
  </div>

</main>
</body>
</html>
```